Eyecatching Carpentry Business card

I need a business card designed for myself, my company name is Tom Hadfield Carpentry.
I am based on the south coast of England and I do all aspects of carpentry, including;
skirting
Architraves
kitchens
roof construction
flooring
doors
loft conversions
decking
windows
I currently have no company logo or letter head so I leave all design ideas to designers.
All I ask is that it looks professional and modern.
A logo may be incorporated as well.
My contact details should be on the back, telephone and email.

```html
<!DOCTYPE html>
<html lang="en">
<head>
<meta charset="utf-8">
<title>Tom Hadfield Carpentry – Business Card</title>
<link rel="stylesheet" href="https://fonts.googleapis.com/css2?family=Arimo:wght@400;700&family=Kaushan+Script&display=swap">
<style>
  :root {
    --page-bg: #e6e3df;
    --oak-light: #f2c995;
    --oak-mid: #e8b07a;
    --oak-deep: #d89a60;
    --ink: #1c1712;
    --ink-faint: rgba(70, 45, 20, 0.17);
    --card-shadow: rgba(40, 30, 20, 0.24);
  }
  * { margin: 0; padding: 0; box-sizing: border-box; }
  html, body {
    width: 1200px;
    height: 873px;
    overflow: hidden;
    background: var(--page-bg);
  }
  .canvas {
    width: 1200px;
    height: 873px;
    display: flex;
    align-items: center;
    justify-content: center;
    gap: 60px;
  }
  .card {
    position: relative;
    width: 520px;
    height: 298px;
    border-radius: 4px;
    overflow: hidden;
    box-shadow: 0 10px 28px var(--card-shadow);
  }
  .card__wood {
    position: absolute;
    inset: 0;
    background:
      linear-gradient(180deg, rgba(255, 235, 205, 0.18) 0%, rgba(255, 235, 205, 0) 40%, rgba(150, 90, 40, 0.08) 100%),
      linear-gradient(160deg, var(--oak-light) 0%, var(--oak-mid) 55%, var(--oak-deep) 100%);
  }

  /* Front */
  .front__mark {
    position: absolute;
    left: 0;
    right: 0;
    top: 120px;
    display: flex;
    justify-content: center;
    align-items: center;
    gap: 12px;
    padding-left: 60px;
    font-family: "Arimo", sans-serif;
    font-weight: 700;
    font-size: 26px;
    color: var(--ink);
  }
  .front__mark-square {
    width: 26px;
    height: 26px;
    background: var(--ink);
  }
  .front__company {
    position: absolute;
    left: 105px;
    top: 196px;
    font-family: "Kaushan Script", cursive;
    font-weight: 400;
    font-size: 34px;
    line-height: 1;
    color: var(--ink);
  }
  .front__rule {
    position: absolute;
    left: 40px;
    right: 50px;
    top: 246px;
    height: 1px;
    background: var(--ink);
  }

  /* Back */
  .back__details {
    position: absolute;
    left: 34px;
    top: 30px;
    font-family: "Arimo", sans-serif;
    color: var(--ink);
  }
  .back__name { font-size: 26px; line-height: 1; }
  .back__title { font-size: 13px; margin-top: 3px; }
  .back__address { font-size: 16px; margin-top: 20px; line-height: 1.2; }
  .back__phone { font-size: 16px; margin-top: 18px; }
  .back__email { font-size: 16px; margin-top: 26px; }
  .back__faint-name {
    position: absolute;
    left: 250px;
    top: 150px;
    display: flex;
    align-items: center;
    gap: 12px;
    font-family: "Arimo", sans-serif;
    font-weight: 700;
    font-size: 28px;
    color: var(--ink-faint);
  }
  .back__faint-square {
    width: 28px;
    height: 28px;
    background: var(--ink-faint);
  }
</style>
</head>
<body>
  <main class="canvas">
    <section class="card card--back" aria-label="Card back">
      <div class="card__wood" role="img" aria-label="Light oak wood grain texture"></div>
      <div class="back__details">
        <p class="back__name">Your Name</p>
        <p class="back__title">Your Title</p>
        <p class="back__address">Sample Address<br>Sample Street</p>
        <p class="back__phone">123456789</p>
        <p class="back__email">sample@sample.com</p>
      </div>
      <div class="back__faint-name">
        <span class="back__faint-square"></span>
        <span>Tom Hadfield</span>
      </div>
    </section>

    <section class="card card--front" aria-label="Card front">
      <div class="card__wood" role="img" aria-label="Light oak wood grain texture"></div>
      <div class="front__mark">
        <span class="front__mark-square"></span>
        <span>Tom Hadfield</span>
      </div>
      <h1 class="front__company">Tom Hadfield Carpentry</h1>
      <div class="front__rule"></div>
    </section>
  </main>
</body>
</html>
```